Fresh looking flyer for Vellmar Institute Of Computing

We need a flyer design for our IT school that will be distributed to potential students during our recruitment campaign. We want to feature the following aspects of the school:

-Study IT in a nordic/european way close to your home (design should feel Scandinavian)
-Featuring the dean of the school (photo attached)
-Match the theme of logo (logo attached)
-A potential layout attached as a mockup

CONTENT
* Main Message " LEARN EUROPEAN PROGRAMMING COURSES IN BEKASI"
* Sub Message " 3 MONTH MODULES FROM BEGINNER TO ADVANCED"
* Campaign " ATTEND FREE CLASS & GET 10% OFF COURSE, SIGN UP BETWEEN 7-18MARCH. vellmar.example/free
* Extra info: " GRADUATE AND GET HIRED TO EARN 120 MILLION IDR/YEAR"

End result should be in Adobe Illustrator format.

Target Market(s)

18-30 year old Indonesians interested in IT

Industry/Entity Type

Education

Font styles to use
Sans Serif

Colors
85cae6

Requirements
Must have
• -Photo of the manager
• -Messages as in the project description
• -School logo
• -Nordic look and feel

```html
<!DOCTYPE html>
<html lang="en">
<head>
<meta charset="utf-8">
<title>Vellmar Institute Of Computing – Flyer</title>
<link href="https://fonts.googleapis.com/css2?family=Josefin+Sans:wght@300;400;600&family=Montserrat:wght@400;600;800&family=Bebas+Neue&display=swap" rel="stylesheet">
<style>
  :root{
    --sky:#bfe9fb;
    --navy:#123a6d;
    --navy-deep:#0b1f52;
    --ink:#111111;
    --blue:#2bb3e6;
    --brand:#85cae6;
    --white:#ffffff;
    --photo-a:#c9c4bf;
    --photo-b:#5a6478;
  }
  *{margin:0;padding:0;box-sizing:border-box}
  html,body{width:1200px;height:1200px;overflow:hidden;background:var(--sky)}
  .flyer{position:absolute;left:190px;top:20px;width:820px;height:1160px;overflow:hidden;background:var(--white);box-shadow:0 12px 40px rgba(11,31,82,.25)}
  .flyer-shapes{position:absolute;inset:0}
  .abs{position:absolute}

  .brand{left:20px;top:40px;width:380px;text-align:center;color:var(--white)}
  .brand-mark{width:56px;height:56px;border:2px solid var(--white);border-radius:50%;margin:0 auto 18px}
  .brand-name{font-family:"Josefin Sans",sans-serif;font-weight:600;font-size:27px;line-height:32px;letter-spacing:1px;text-transform:uppercase}

  .headline{left:56px;top:272px;font-family:"Josefin Sans",sans-serif;font-weight:300;font-size:42px;line-height:46px;color:var(--navy);text-transform:uppercase}
  .headline .hl{color:var(--white);font-weight:400}

  .modules{left:34px;top:458px;color:var(--white);text-transform:uppercase}
  .modules-title{font-family:"Josefin Sans",sans-serif;font-weight:400;font-size:40px;line-height:42px}
  .modules-sub{font-family:"Josefin Sans",sans-serif;font-weight:400;font-size:21px;letter-spacing:.5px}

  .campaign{left:0;width:820px;text-align:center;text-transform:uppercase}
  .banner{top:632px;font-family:"Bebas Neue",sans-serif;font-size:38px;color:var(--white);letter-spacing:.5px}
  .offer{top:684px;font-family:"Montserrat",sans-serif;font-weight:800;font-size:38px;color:var(--white)}
  .signup{top:734px;font-family:"Josefin Sans",sans-serif;font-weight:400;font-size:32px;color:var(--blue)}
  .dates{top:768px;font-family:"Montserrat",sans-serif;font-weight:800;font-size:40px;color:var(--blue)}
  .url{top:828px;font-family:"Montserrat",sans-serif;font-weight:400;font-size:30px;color:var(--white);text-transform:none}
  .hired{top:906px;font-family:"Josefin Sans",sans-serif;font-weight:400;font-size:32px;color:var(--white)}
  .salary{top:948px;font-family:"Montserrat",sans-serif;font-weight:800;font-size:36px;color:var(--white)}

  .contact{left:40px;top:1040px;width:740px;display:flex;align-items:center;color:var(--white);font-family:"Montserrat",sans-serif;font-size:13px;line-height:18px}
  .contact-item{display:flex;align-items:center;gap:10px;padding:0 18px}
  .contact-item + .contact-item{border-left:1px solid var(--blue);height:56px}
  .contact-item svg{flex:none}
  .contact-address{flex:1.7;padding-left:0}
  .contact-phone,.contact-mail{flex:1}
</style>
</head>
<body>
<main class="flyer">
  <svg class="flyer-shapes" width="820" height="1160" viewBox="0 0 820 1160">
    <defs>
      <linearGradient id="photoTone" x1="0" y1="0" x2="1" y2="1">
        <stop offset="0" stop-color="var(--photo-a)"/>
        <stop offset="1" stop-color="var(--photo-b)"/>
      </linearGradient>
      <clipPath id="portraitClip"><circle cx="690" cy="230" r="280"/></clipPath>
    </defs>

    <!-- right navy backdrop -->
    <path d="M540 390 L820 300 V660 H540 Z" fill="var(--navy)"/>

    <!-- header block -->
    <path d="M0 0 H460 V220 L0 196 Z" fill="var(--navy)"/>
    <path d="M250 206 L460 218 L445 250 Z" fill="var(--blue)"/>

    <!-- portrait -->
    <circle cx="690" cy="230" r="286" fill="var(--white)"/>
    <g clip-path="url(#portraitClip)" role="img" aria-label="Portrait of the school dean smiling in glasses and white shirt, with a student coding on a laptop behind">
      <rect x="400" y="-60" width="600" height="580" fill="url(#photoTone)"/>
    </g>

    <!-- headline accents -->
    <rect x="40" y="270" width="3" height="190" fill="var(--navy)"/>
    <path d="M50 364 H492 L522 410 H50 Z" fill="var(--blue)"/>

    <!-- modules ribbon -->
    <path d="M0 452 H548 L575 500 L548 548 H0 Z" fill="var(--navy)"/>

    <!-- lower section -->
    <path d="M0 712 Q400 560 820 620 V1160 H0 Z" fill="var(--blue)"/>
    <path d="M0 730 Q400 580 820 640 V1160 H0 Z" fill="var(--navy-deep)"/>
    <line x1="0" y1="700" x2="220" y2="690" stroke="var(--ink)" stroke-width="3"/>
    <line x1="600" y1="674" x2="820" y2="664" stroke="var(--ink)" stroke-width="3"/>
    <path d="M200 632 L630 618 L618 676 L212 690 Z" fill="var(--ink)"/>

    <!-- url band -->
    <path d="M0 830 Q410 800 820 812 V872 Q410 860 0 890 Z" fill="var(--blue)"/>

    <!-- footer rule -->
    <line x1="40" y1="1012" x2="780" y2="1012" stroke="var(--blue)" stroke-width="1"/>
  </svg>

  <div class="abs brand">
    <div class="brand-mark"></div>
    <div class="brand-name">Vellmar Institute<br>Of Computing</div>
  </div>

  <h1 class="abs headline">Learn<br>European<br><span class="hl">Programming</span><br>Courses in Bekasi</h1>

  <div class="abs modules">
    <div class="modules-title">3 Month Modules</div>
    <div class="modules-sub">From beginner to advanced</div>
  </div>

  <div class="abs campaign banner">Attend free class &amp;</div>
  <div class="abs campaign offer">Get 10% off course,</div>
  <div class="abs campaign signup">Sign up between</div>
  <div class="abs campaign dates">7-18 March.</div>
  <div class="abs campaign url">vellmar.example/free</div>
  <div class="abs campaign hired">Graduate and get hired</div>
  <div class="abs campaign salary">To earn 120 million IDR/year</div>

  <footer class="abs contact">
    <div class="contact-item contact-address">
      <svg width="18" height="24" viewBox="0 0 18 24"><path d="M9 0a9 9 0 0 1 9 9c0 6-9 15-9 15S0 15 0 9a9 9 0 0 1 9-9z" fill="var(--blue)"/><circle cx="9" cy="9" r="3.5" fill="var(--navy-deep)"/></svg>
      <span>Jl. Taman Lestari No. 48, Blok C-07<br>Kota Bekasi, Jawa Barat 17110</span>
    </div>
    <div class="contact-item contact-phone">
      <svg width="16" height="26" viewBox="0 0 16 26"><rect x="1" y="1" width="14" height="24" rx="3" fill="none" stroke="var(--blue)" stroke-width="2"/><circle cx="8" cy="21" r="1.5" fill="var(--blue)"/></svg>
      <span>+62 811-5550-0192</span>
    </div>
    <div class="contact-item contact-mail">
      <svg width="24" height="18" viewBox="0 0 24 18"><rect x="0" y="0" width="24" height="18" rx="2" fill="var(--blue)"/><path d="M1 2 L12 10 L23 2" fill="none" stroke="var(--navy-deep)" stroke-width="2"/></svg>
      <span>admin@vellmar.example</span>
    </div>
  </footer>
</main>
</body>
</html>
```